Mexican construction company needs a business card design

We need a business card design for a company based in Monterrey, Mexico called:

Desarrollos Tolvani S.A. de C.V.

The company is in the construction business and I would like the businees card to be simple and concise. Please use white background and blue or black text color that say:

"Proyectos de Construcción"-- (Brief description of business)
" Rodrigo Ulloa Benítez"--- (My name)
"rulloab@correovelo.mx"-- (My email)
"C: (81) 82 19 57 46"-- (My cell)
"O: (81) 86 72 13 95"-- (Office phone)

Please use only the colors of my company that are attached

Please make the back of the business card blue (same blue from logo) and use the logo.

Thanks!

```html
<!DOCTYPE html>
<html lang="es">
<head>
<meta charset="utf-8">
<title>Desarrollos Tolvani — Tarjeta de presentación</title>
<link rel="stylesheet" href="https://fonts.googleapis.com/css2?family=Nunito+Sans:wght@400;600;800&display=swap">
<style>
  :root {
    --stage: #2b2b2e;
    --paper: #f7f7f8;
    --paper-shade: #e9e9ec;
    --navy: #2e2f6b;
    --charcoal: #3a3b3e;
    --panel: #38393c;
    --panel-edge: #4a4b4f;
    --map-tone: #ececef;
    --map-tone-dark: #444549;
    --ink: #1f2024;
    --ink-soft: #4a4b50;
    --panel-text: #e6e6e8;
  }
  * { box-sizing: border-box; margin: 0; padding: 0; }
  html, body { width: 1200px; height: 800px; overflow: hidden; }
  body {
    background: var(--stage);
    font-family: "Nunito Sans", Arial, sans-serif;
    position: relative;
  }
  .card {
    position: absolute;
    width: 525px;
    height: 300px;
    background: linear-gradient(160deg, #ffffff 0%, var(--paper) 55%, var(--paper-shade) 100%);
    overflow: hidden;
    box-shadow: 0 18px 40px rgba(0,0,0,.45);
  }
  .card-front { left: 70px; top: 120px; }
  .card-back  { left: 605px; top: 380px; }

  .card-shapes { position: absolute; inset: 0; width: 100%; height: 100%; }

  .world-map {
    position: absolute;
    left: 120px; top: 70px;
    width: 290px; height: 160px;
    border-radius: 40px;
    background: radial-gradient(ellipse at center, var(--map-tone) 0%, rgba(236,236,239,0) 72%);
  }

  .brand {
    position: absolute;
    left: 0; right: 0; top: 128px;
    display: flex; align-items: center; justify-content: center; gap: 14px;
  }
  .brand-square {
    width: 38px; height: 38px;
    background: var(--navy);
  }
  .brand-name {
    font-weight: 800;
    font-size: 30px;
    letter-spacing: .5px;
    color: var(--navy);
    text-transform: uppercase;
    line-height: 1;
  }

  .contact-panel {
    position: absolute;
    left: 28px; top: 96px;
    width: 240px; height: 176px;
    border-radius: 10px;
    background: var(--panel);
    border: 1px solid var(--panel-edge);
    overflow: hidden;
    color: var(--panel-text);
    text-align: center;
    font-size: 12px;
    line-height: 1.25;
  }
  .panel-map {
    position: absolute; inset: 10px 14px;
    border-radius: 30px;
    background: radial-gradient(ellipse at center, var(--map-tone-dark) 0%, rgba(68,69,73,0) 75%);
  }
  .contact-icon {
    position: relative;
    display: block;
    width: 22px; height: 22px;
    margin: 0 auto 5px;
  }
  .contact-phones { position: relative; margin-top: 16px; }
  .contact-email  { position: relative; margin-top: 18px; }
  .contact-line { display: block; }

  .holder {
    position: absolute;
    left: 300px; top: 94px;
    width: 210px;
    text-align: center;
  }
  .holder-name {
    font-weight: 800;
    font-size: 19px;
    line-height: 1.15;
    color: var(--ink);
  }
  .holder-role {
    margin-top: 4px;
    font-weight: 400;
    font-size: 11.5px;
    color: var(--ink-soft);
  }
</style>
</head>
<body>

  <section class="card card-front" aria-label="Frente de la tarjeta">
    <svg class="card-shapes" viewBox="0 0 525 300" aria-hidden="true">
      <polygon points="0,62 48,62 98,150 48,238 0,238" fill="var(--navy)"/>
      <polygon points="525,180 525,300 470,300 440,222" fill="var(--navy)"/>
    </svg>
    <div class="world-map" role="img" aria-label="Mapa mundial punteado de fondo, gris muy claro"></div>
    <div class="brand">
      <span class="brand-square" aria-hidden="true"></span>
      <span class="brand-name">Desarrollos Tolvani</span>
    </div>
  </section>

  <section class="card card-back" aria-label="Reverso de la tarjeta">
    <svg class="card-shapes" viewBox="0 0 525 300" aria-hidden="true">
      <path d="M55,0 L92,0 C100,110 120,210 150,300 L112,300 C88,210 66,110 55,0 Z" fill="var(--navy)"/>
      <path d="M100,0 L118,0 C112,90 150,200 195,300 L178,300 C130,210 98,100 100,0 Z" fill="var(--charcoal)"/>
      <path d="M176,0 L185,0 C178,90 205,190 232,262 C200,200 172,100 176,0 Z" fill="var(--charcoal)"/>
    </svg>

    <div class="contact-panel">
      <div class="panel-map" role="img" aria-label="Mapa mundial punteado en gris oscuro"></div>
      <div class="contact-phones">
        <svg class="contact-icon" viewBox="0 0 22 22" aria-hidden="true">
          <rect x="1" y="1" width="20" height="20" rx="3" fill="none" stroke="#e6e6e8" stroke-width="1.4"/>
          <path d="M7.5,5.5 l2,0 l1,3 l-1.3,1 c.7,1.5 1.8,2.6 3.3,3.3 l1,-1.3 l3,1 l0,2 c0,.8 -.7,1.3 -1.5,1.3 c-4.5,-.4 -8.4,-4.3 -8.8,-8.8 c0,-.8 .5,-1.5 1.3,-1.5 z" fill="#e6e6e8"/>
        </svg>
        <span class="contact-line">C: (81) 82 19 57 46</span>
        <span class="contact-line">O: (81) 86 72 13 95</span>
      </div>
      <div class="contact-email">
        <svg class="contact-icon" viewBox="0 0 22 22" aria-hidden="true">
          <rect x="1" y="1" width="20" height="20" rx="3" fill="none" stroke="#e6e6e8" stroke-width="1.4"/>
          <rect x="5" y="7" width="12" height="8.5" fill="#e6e6e8"/>
          <path d="M5,7 L11,12 L17,7" fill="none" stroke="#38393c" stroke-width="1.2"/>
        </svg>
        <span class="contact-line">rulloab@correovelo.mx</span>
      </div>
    </div>

    <div class="holder">
      <h1 class="holder-name">Rodrigo<br>Ulloa Benítez</h1>
      <p class="holder-role">Proyectos de Construcción</p>
    </div>
  </section>

</body>
</html>
```